依頼詳細
■ターゲット層
20代後半~30代前半
女性、子連れもOK
※地域的に富裕層の方が多いのでそういったお客様層を囲い込みたいです。

■サイトマップ
①トップ
②メニュー&プライス
③スタッフ
④サロンインフォ
⑤コンセプト
⑥お客様の声
⑦ブログ
⑧ニュース
⑨スタイルギャラリー
⑩リクルート
⑪商品紹介
⑫お問い合わせ
⑬サイトマップ

■取り入れてほしい物
・Snapvela
・ヘア予約入り口
・リクルートコンテンツの強化
・お子様連れを強化しているという点
ただ、子供っぽくはなり過ぎたくないです。

■参考サイト
http://www.morvantide.com/(このサイトは全体的に好きです。)
http://75kites.com/(書体のはずしと空間の使い方が全体的に好きです)

■カラー・テイスト
カラー :木の感じ / クリーム / 濁った青色(サロンカードカラー)
テイスト:ナチュラル / 優しい / シンプル / 清潔な

【素材について】
①内観・外観・スタイル写真・ロゴなど
枚数が多いため下記よりダウンロードしてご使用ください。
http://7.bulkdorani.jp/0412-b8e2f1a9c3d7e6054a1b2c9d8e7f6a5b4
(保存期間21日間)

②その他素材
今回、ストクヴァン「https://jp.stockvarine.com/」にて 制作中の間定期契約しています。
デザインの際には、一度仮素材にて配置を頂き、ストクヴァン以外の素材は無料の物をご使用頂きたいです。
ページ数
1ページ
希望イメージ
シンプル 複雑
単色 カラフル
暗い 明るい
日常 高級
遊び心 厳粛
未来的 伝統的
女性的 男性的
希望する色
青系、木の感じ / クリーム / 濁った青色(サロンカードカラー)
納品ファイル
• 高解像度JPG (.jpg)
• イラストレーター形式 (.ai)
• フォトショップ形式 (.psd)
• PNG形式 (.png)
もう少しデザインを見たいため、申し訳ありませんが1週間期間を延長致します。
宜しくお願い致します。

柔らかい印象、落ち着いた印象がきっちろ表現されていてとても気に入っています。

沢山のご提案をくださり、誠にありがとうございました。

```html
<!DOCTYPE html>
<html lang="ja">
<head>
<meta charset="utf-8">
<title>hair salon Luneva</title>
<link rel="stylesheet" href="https://fonts.googleapis.com/css2?family=Cormorant+Garamond:wght@300;400;500&family=Noto+Serif+JP:wght@300;400;500&display=swap">
<style>
  :root {
    --cream: #fbf6c4;
    --ink: #6d6a5c;
    --ink-soft: #a29e88;
    --line: #e2d98e;
    --sky: #e8f6f4;
    --bg-top: #eef1ee;
    --bg-mid: #f6f7f4;
    --bg-low: #f2f4f0;
    --footer: #fbf3b0;
    --footer-base: #e9dd86;
    --badge-frame: #a8c79b;
    --nav-bg: rgba(255,255,255,.72);
  }
  * { box-sizing: border-box; margin: 0; padding: 0; }
  html, body { width: 1200px; height: 3208px; overflow: hidden; }
  body {
    position: relative;
    font-family: "Noto Serif JP", serif;
    color: var(--ink);
    background: linear-gradient(180deg, var(--bg-top) 0%, var(--bg-mid) 30%, #fbfbf8 55%, var(--bg-low) 85%, #eef0ea 100%);
  }
  .abs { position: absolute; }
  .photo { position: absolute; }

  /* top navigation */
  .top-nav { position: absolute; z-index: 10; left: 0; top: 0; width: 1200px; height: 26px; background: var(--nav-bg); }
  .top-nav .brand { position: absolute; left: 22px; top: 4px; font-family: "Cormorant Garamond", serif; font-size: 15px; color: var(--ink); }
  .top-nav ul { position: absolute; left: 230px; top: 5px; display: flex; gap: 30px; list-style: none; font-family: "Cormorant Garamond", serif; font-size: 14px; letter-spacing: .12em; color: var(--ink); }

  /* hero */
  .hero-photo { left: 0; top: 0; width: 760px; height: 520px; background: linear-gradient(160deg, #e4e6e2 0%, #c8ccc6 40%, #b6bdb0 75%, #d9dcd4 100%); }
  .hero-panel { left: 620px; top: 0; width: 580px; height: 520px; }
  .hero-mark { left: 720px; top: 170px; font-family: "Cormorant Garamond", serif; font-weight: 300; font-size: 150px; line-height: 1; color: #efe6a0; letter-spacing: .02em; }
  .hero-sub { left: 690px; top: 36px; font-family: "Cormorant Garamond", serif; font-size: 22px; color: #d9cf86; letter-spacing: .1em; }
  .hero-copy { left: 820px; top: 54px; width: 360px; font-size: 29px; line-height: 1.9; color: #8a8470; letter-spacing: .12em; }
  .reserve { left: 944px; top: 368px; width: 236px; height: 148px; background: #fffde9; border: 10px solid var(--badge-frame); text-align: center; padding-top: 14px; }
  .reserve .en { font-family: "Cormorant Garamond", serif; font-size: 30px; color: #5f7a55; }
  .reserve .jp { font-size: 17px; line-height: 1.5; color: #5f6a4a; margin-top: 4px; }

  .section-title { position: absolute; left: 0; width: 1200px; text-align: center; font-family: "Cormorant Garamond", serif; font-size: 26px; letter-spacing: .12em; color: var(--ink); }

  .menu-grid { left: 168px; top: 664px; width: 864px; height: 512px; display: grid; grid-template-columns: repeat(4, 216px); grid-template-rows: repeat(2, 256px); }
  .menu-card { background: var(--cream); display: flex; flex-direction: column; align-items: center; justify-content: center; gap: 22px; padding: 0 18px; text-align: center; }
  .menu-card .note { font-size: 13px; line-height: 1.7; color: var(--ink-soft); }
  .btn { display: inline-block; border: 1px solid var(--line); padding: 8px 22px; font-family: "Cormorant Garamond", serif; font-size: 20px; color: var(--ink-soft); background: rgba(255,255,255,.25); }

  .family-card { background: var(--cream); display: flex; flex-direction: column; align-items: center; justify-content: center; gap: 26px; padding: 0 16px; text-align: center; }
  .family-card .note { font-size: 15px; line-height: 1.8; color: var(--ink-soft); }

  .feed { left: 168px; top: 2096px; width: 864px; height: 404px; background: var(--sky); }
  .feed-item { position: absolute; top: 18px; }
  .feed-item .shot { width: 100%; height: 280px; }
  .feed-item .cap { font-size: 12px; line-height: 1.6; color: var(--ink-soft); margin-top: 14px; }

  .recruit-strip { left: 168px; top: 2652px; width: 864px; height: 300px; }

  .site-footer { left: 0; top: 3030px; width: 1200px; height: 150px; background: var(--footer); }
  .footer-brand { left: 205px; top: 3060px; font-family: "Cormorant Garamond", serif; font-size: 22px; color: var(--ink); }
  .footer-address { left: 205px; top: 3092px; font-size: 11px; line-height: 1.7; color: var(--ink); }
  .footer-nav { left: 470px; display: flex; gap: 44px; font-family: "Cormorant Garamond", serif; font-size: 17px; letter-spacing: .1em; color: var(--ink); list-style: none; }
  .copyright { left: 0; top: 3180px; width: 1200px; height: 28px; background: var(--footer-base); text-align: center; font-family: "Cormorant Garamond", serif; font-size: 14px; line-height: 28px; color: var(--ink); letter-spacing: .06em; }
</style>
</head>
<body>

<header>
  <div class="photo hero-photo" role="img" aria-label="Salon storefront with white facade, shop signboard and potted plants"></div>
  <svg class="abs hero-panel" width="580" height="520" viewBox="0 0 580 520" aria-hidden="true">
    <path d="M80 0 H580 V520 H0 C70 420 20 300 60 200 C90 120 40 60 80 0 Z" fill="#fbf6c4"/>
  </svg>
  <div class="abs hero-sub">hair salon</div>
  <div class="abs hero-mark">Luneva</div>
  <p class="abs hero-copy">あなたの想いを、<br>「カタチ」にする</p>
  <a class="abs reserve">
    <div class="en">Reserved</div>
    <div class="jp">WEB予約は、<br>こちらをクリック</div>
  </a>
</header>

<nav class="top-nav">
  <span class="brand">Luneva</span>
  <ul>
    <li>MENU</li><li>STAFF</li><li>INFO</li><li>CONCEPT</li><li>BLOG</li><li>NEWS</li><li>GALLALY</li><li>PRODUCT</li><li>RECRUIT</li>
  </ul>
</nav>

<h2 class="section-title" style="top:592px;">MENU</h2>
<section class="abs menu-grid">
  <div class="photo" style="position:static;background:linear-gradient(150deg,#e6d2bf,#b88a66);" role="img" aria-label="Medium hairstyle portrait"></div>
  <div class="menu-card"><p class="note">ふんわり軽やかな<br>大人ミディアム</p><span class="btn">Medium hair</span></div>
  <div class="photo" style="position:static;background:linear-gradient(150deg,#ece6e2,#9a877c);" role="img" aria-label="Bob hairstyle portrait"></div>
  <div class="menu-card"><p class="note">まとまりやすい<br>上品なボブスタイル</p><span class="btn">Bob hair</span></div>
  <div class="menu-card"><p class="note">艶やかに揺れる<br>ロングヘア</p><span class="btn">Long hair</span></div>
  <div class="photo" style="position:static;background:linear-gradient(150deg,#f1e3df,#6a4a44);" role="img" aria-label="Long hairstyle portrait"></div>
  <div class="menu-card"><p class="note">すっきり爽やかな<br>ショートスタイル</p><span class="btn">Short hair</span></div>
  <div class="photo" style="position:static;background:linear-gradient(150deg,#f0ece4,#5e5048);" role="img" aria-label="Short hairstyle portrait"></div>
</section>

<h2 class="section-title" style="top:1222px;">For Mama and Kids</h2>
<div class="photo" style="left:168px;top:1280px;width:592px;height:368px;background:linear-gradient(120deg,#ece8e4,#c9b4a4 55%,#8a6a58);" role="img" aria-label="Stylist combing a smiling mother's long hair"></div>
<div class="abs family-card" style="left:760px;top:1280px;width:272px;height:262px;">
  <p class="note">お母さんのご来店も<br>ゆったりお過ごしいただけます</p>
  <span class="btn">For Mama</span>
</div>
<div class="abs family-card" style="left:168px;top:1648px;width:272px;height:318px;">
  <p class="note">キッズスペースで<br>お子様も安心して<br>お待ちいただけます</p>
  <span class="btn">For Kids</span>
</div>
<div class="photo" style="left:440px;top:1648px;width:592px;height:318px;background:linear-gradient(120deg,#dfe6d2,#b8c7a6 40%,#8fa7c0);" role="img" aria-label="Two young boys smiling together indoors"></div>

<h2 class="section-title" style="top:2010px;">Snapvela</h2>
<section class="abs feed">
  <div class="feed-item" style="left:18px;width:262px;">
    <div class="shot" style="background:linear-gradient(160deg,#c9c2c0,#4c4448);" role="img" aria-label="Braided updo hairstyle from behind"></div>
    <p class="cap">2018.05.12<br>いまどき編み込みアレンジ</p>
  </div>
  <div class="feed-item" style="left:298px;width:262px;">
    <div class="shot" style="background:linear-gradient(160deg,#ece4dc,#9c7a64);" role="img" aria-label="Woman relaxing during a head spa treatment"></div>
    <p class="cap">2018.05.08<br>【新着】ヘッドスパで癒しの時間を</p>
  </div>
  <div class="feed-item" style="left:578px;width:268px;">
    <div class="shot" style="height:230px;background:linear-gradient(160deg,#f4f4f2,#d2d0cc);" role="img" aria-label="Hair care product bottles and a portrait on a shelf"></div>
    <p class="cap">サロンおすすめヘアケア商品</p>
    <span class="btn" style="margin:10px 0 0 70px;font-size:16px;padding:6px 18px;">more detail</span>
  </div>
</section>

<h2 class="section-title" style="top:2594px;">Recruit</h2>
<div class="photo recruit-strip" style="background:linear-gradient(90deg,#dfe8dc 0%,#c9dcc2 35%,#eaf2e2 60%,#c4d8a8 100%);" role="img" aria-label="Salon interior with plants and a smiling staff member in a green field"></div>

<footer>
  <div class="abs site-footer"></div>
  <div class="abs footer-brand">Luneva</div>
  <p class="abs footer-address">東京都港区白金台1-2-3 ルネヴァ1F<br>お問い合わせ 03-0000-0000<br>営業時間 10:00-20:00 定休日 火曜日</p>
  <ul class="abs footer-nav" style="top:3072px;"><li>MENU</li><li>STAFF</li><li>INFO</li><li>CONCEPT</li><li>VOICE</li></ul>
  <ul class="abs footer-nav" style="top:3110px;"><li>BLOG</li><li>NEWS</li><li>GALLALY</li><li>PRODUCT</li><li>RECRUIT</li><li>MAIL</li></ul>
  <div class="abs copyright">copyright© hair salon Luneva All right reserved</div>
</footer>

</body>
</html>
```